Business card design and logo needed

We have been operating as Ridgeline Posts for 30 years but never had a logo and feel there is a need for one, but have no idea for a design.
We specialise in all types of rural fencing including post and wire, post and rail, electric, chainmesh and to a lesser extent, also do industrial security fencing.
Updates

Sorry, but website is ridgelineposts.example

No .au on the end!
My apologies

Regards, Darren

Target Market(s)

Rural/acreage property owners, particularly horse people.

Industry/Entity Type

Industrial

Contact Information for Business Card

Ridgeline Posts Darren Kellett 0499 572106. Lewis Kellett 0499 613720
Email: ridgelineposts@mailhub.example
Website: www.ridgelineposts.example.au

Requirements
Must have
• Would like to highlight website address - use the business card to advertise the website or to push them to check it out.

```html
<!DOCTYPE html>
<html lang="en">
<head>
<meta charset="utf-8">
<title>Ridgeline Posts – Business Card</title>
<link rel="stylesheet" href="https://fonts.googleapis.com/css2?family=Open+Sans:wght@400;600;700&display=swap">
<style>
  :root {
    --stage: #e4e6e6;
    --stage-edge: #c9cccc;
    --card: #171b1b;
    --card-band: #1e2523;
    --curve-line: #5a5f5d;
    --ink-light: #eef0ef;
    --ink-soft: #c9cccb;
    --ink-muted: #8d9190;
    --accent: #e17b12;
  }
  * { box-sizing: border-box; margin: 0; padding: 0; }
  html, body {
    width: 1200px; height: 741px; overflow: hidden;
  }
  body {
    background: radial-gradient(ellipse at 50% 40%, var(--stage) 0%, var(--stage-edge) 100%);
    font-family: "Open Sans", Arial, sans-serif;
    position: relative;
  }
  .card {
    position: absolute;
    top: 216px;
    width: 540px;
    height: 309px;
    background: var(--card);
    overflow: hidden;
    box-shadow: 0 10px 24px rgba(0,0,0,0.28);
  }
  .card--back { left: 40px; }
  .card--front { left: 620px; }

  .back-website {
    position: absolute;
    left: 0; right: 0; top: 50%;
    transform: translateY(-50%);
    text-align: center;
    color: var(--accent);
    font-size: 14px;
    letter-spacing: 2px;
  }

  .front-band { position: absolute; left: 0; top: 0; width: 540px; height: 309px; }

  .brand {
    position: absolute;
    left: 0; right: 0; top: 78px;
    display: flex; justify-content: center; align-items: center; gap: 10px;
  }
  .brand-mark {
    width: 12px; height: 12px; background: var(--ink-muted);
  }
  .brand-name {
    color: var(--ink-muted);
    font-size: 22px;
    font-weight: 400;
    letter-spacing: 0.5px;
  }

  .contacts {
    position: absolute;
    left: 0; right: 0; top: 186px;
    display: flex; justify-content: center; align-items: flex-start;
  }
  .contact { width: 200px; text-align: center; }
  .contact-name {
    color: var(--ink-light);
    font-size: 19px;
    font-weight: 700;
    line-height: 1.2;
  }
  .contact-phone {
    color: var(--ink-soft);
    font-size: 12px;
    margin-top: 3px;
    display: flex; justify-content: center; align-items: center; gap: 6px;
  }
  .divider {
    width: 1px; height: 50px; background: var(--ink-soft); margin: 0 16px;
  }
  .links {
    position: absolute;
    left: 150px; top: 252px;
  }
  .link-row {
    display: flex; align-items: center; gap: 10px;
    font-size: 12px; line-height: 20px;
  }
  .link-row--email { color: var(--ink-soft); }
  .link-row--web { color: var(--accent); }
  .icon { width: 13px; height: 13px; flex: none; }
</style>
</head>
<body>

  <section class="card card--back" aria-label="Card back">
    <p class="back-website">www.ridgelineposts.example</p>
  </section>

  <section class="card card--front" aria-label="Card front">
    <svg class="front-band" viewBox="0 0 540 309" aria-hidden="true">
      <path d="M0,0 H540 V40 Q380,175 90,165 Q40,163 0,158 Z" fill="var(--card-band)"/>
      <path d="M20,160 Q60,164 95,165 Q380,175 540,40" fill="none" stroke="var(--curve-line)" stroke-width="2"/>
    </svg>

    <div class="brand">
      <span class="brand-mark"></span>
      <span class="brand-name">Ridgeline Posts</span>
    </div>

    <div class="contacts">
      <div class="contact">
        <p class="contact-name">Darren Kellett</p>
        <p class="contact-phone">
          <svg class="icon" viewBox="0 0 16 16" aria-hidden="true"><path d="M2 6 Q8 1 14 6 L12 8 L10 6.5 H6 L4 8 Z M4 9 H12 L13 14 H3 Z" fill="var(--ink-muted)"/></svg>
          0499 572106
        </p>
      </div>
      <span class="divider"></span>
      <div class="contact">
        <p class="contact-name">Lewis Kellett</p>
        <p class="contact-phone">
          <svg class="icon" viewBox="0 0 16 16" aria-hidden="true"><path d="M2 6 Q8 1 14 6 L12 8 L10 6.5 H6 L4 8 Z M4 9 H12 L13 14 H3 Z" fill="var(--ink-muted)"/></svg>
          0499 613720
        </p>
      </div>
    </div>

    <div class="links">
      <p class="link-row link-row--email">
        <svg class="icon" viewBox="0 0 16 16" aria-hidden="true"><rect x="1.5" y="3.5" width="13" height="9" fill="none" stroke="var(--ink-muted)"/><path d="M1.5 3.5 L8 9 L14.5 3.5" fill="none" stroke="var(--ink-muted)"/></svg>
        ridgelineposts@mailhub.example
      </p>
      <p class="link-row link-row--web">
        <svg class="icon" viewBox="0 0 16 16" aria-hidden="true"><circle cx="8" cy="8" r="6.5" fill="none" stroke="var(--ink-muted)"/><ellipse cx="8" cy="8" rx="3" ry="6.5" fill="none" stroke="var(--ink-muted)"/><path d="M1.5 8 H14.5" stroke="var(--ink-muted)"/></svg>
        www.ridgelineposts.example
      </p>
    </div>
  </section>

</body>
</html>
```